New Meal Prep Flyer for New Package Deals

We are looking for a design that displays our new packages that we offer. If you take a look at our website www.brambleforkmeals.com, and click on packages , you'll see the way we display them currently . We would like something similar to that in style . The first package is called "Horizon" and this package will be a 1 week package (7 days ), 2 meals a day, for a price of $195.00. The second package is called "Amber" and this package will be a 3 week package (21 days) 2 meals per day, for a price of $546.00 , the third package is a 6 week+ package (45 days), and it is called "Evergreen" , 2 meals per day , and the price is $1080.00 .
For the Amber Package , can you put next to it "Save $42.00!"
For the Evergreen Package, can you put next to it "Save $180!"
We also want our logo on the flyer (see attached), and we are just looking for a 1 page flyer , 8 1/2 x 11.

```html
<!DOCTYPE html>
<html lang="en">
<head>
<meta charset="utf-8">
<title>Bramble Fork — Meal Prep Packages</title>
<link href="https://fonts.googleapis.com/css2?family=Arimo:ital,wght@0,400;0,700;1,400&display=swap" rel="stylesheet">
<style>
  :root {
    --paper: #ffffff;
    --brand-green: #7cb62a;
    --green-top: #5a9512;
    --green-bottom: #9fc93c;
    --grey-top: #8e8e8e;
    --grey-bottom: #c6c6c6;
    --orange-top: #e8660a;
    --orange-bottom: #f6b420;
    --price-grey: #8a8a8a;
    --logo-grey: #8c8c8c;
    --white: #ffffff;
  }
  * { box-sizing: border-box; margin: 0; padding: 0; }
  html, body { width: 1074px; height: 1200px; overflow: hidden; background: var(--paper); }
  body { font-family: "Arimo", Arial, sans-serif; position: relative; }

  .brand {
    position: absolute; top: 34px; left: 0; width: 1074px;
    display: flex; flex-direction: column; align-items: center;
  }
  .brand-name {
    display: flex; align-items: center; gap: 16px;
    font-size: 62px; font-weight: 700; color: var(--brand-green);
    letter-spacing: 1px; line-height: 1;
  }
  .brand-dot { width: 26px; height: 26px; border-radius: 50%; background: var(--brand-green); }
  .brand-tagline {
    margin-top: 12px; font-size: 26px; font-weight: 700; color: var(--brand-green);
    letter-spacing: 0.5px;
  }
  .brand-tagline .divider { color: var(--logo-grey); font-weight: 400; margin: 0 10px; }

  .package { position: absolute; color: var(--white); }
  .package-horizon {
    left: 83px; top: 165px; width: 908px; height: 375px;
    border-radius: 40px 0 60px 0;
    background: linear-gradient(to bottom, var(--green-top), var(--green-bottom));
  }
  .package-amber {
    left: 83px; top: 589px; width: 433px; height: 542px;
    border-radius: 0 50px 0 60px;
    background: linear-gradient(to bottom, var(--grey-top), var(--grey-bottom));
  }
  .package-evergreen {
    left: 557px; top: 589px; width: 433px; height: 542px;
    border-radius: 50px 50px 0 60px;
    background: linear-gradient(to bottom, var(--orange-top), var(--orange-bottom));
  }

  .package-title {
    position: absolute; left: 61px; font-size: 46px; font-weight: 700;
    text-transform: uppercase; letter-spacing: 0.5px; line-height: 1;
  }
  .package-length {
    position: absolute; left: 61px; font-size: 31px; font-style: italic; line-height: 1.22;
  }
  .package-meals {
    position: absolute; left: 66px; font-size: 30px; font-weight: 700; line-height: 1;
  }
  .package-price {
    position: absolute; left: 69px; background: var(--white); color: var(--price-grey);
    font-size: 44px; font-weight: 700; line-height: 1;
    display: flex; align-items: center; justify-content: center;
    border-radius: 4px 4px 20px 4px;
  }
  .package-horizon .package-title { top: 62px; }
  .package-horizon .package-length { top: 118px; }
  .package-horizon .package-meals { top: 163px; }
  .package-horizon .package-price { top: 225px; width: 230px; height: 79px; }

  .package-amber .package-title,
  .package-evergreen .package-title { top: 76px; }
  .package-amber .package-length,
  .package-evergreen .package-length { top: 130px; }
  .package-amber .package-meals,
  .package-evergreen .package-meals { top: 234px; }
  .package-amber .package-price { top: 296px; width: 230px; height: 78px; }
  .package-evergreen .package-price { top: 296px; left: 55px; width: 285px; height: 78px; }

  .save-badge {
    position: absolute; width: 148px; height: 148px; border-radius: 50%;
    background: var(--brand-green); border: 5px solid var(--white);
    display: flex; flex-direction: column; align-items: center; justify-content: center;
    color: var(--white); line-height: 1;
  }
  .save-badge .save-label { font-size: 30px; font-weight: 400; letter-spacing: 1px; }
  .save-badge .save-amount { font-size: 46px; font-weight: 700; margin-top: 4px; }
  .package-amber .save-badge { left: 250px; top: 385px; }
  .package-evergreen .save-badge { left: 256px; top: 388px; }
</style>
</head>
<body>
  <header class="brand">
    <div class="brand-name"><span class="brand-dot"></span>BRAMBLE FORK</div>
    <div class="brand-tagline">HEALTHY KITCHEN<span class="divider">|</span>MEAL PREP</div>
  </header>

  <section class="package package-horizon">
    <h2 class="package-title">Horizon</h2>
    <p class="package-length">1 week package&nbsp; (7 days)</p>
    <p class="package-meals">2 meals a day</p>
    <div class="package-price">$195.00</div>
  </section>

  <section class="package package-amber">
    <h2 class="package-title">Amber</h2>
    <p class="package-length">3 week package<br>(21 days)</p>
    <p class="package-meals">2 meals per day</p>
    <div class="package-price">$546.00</div>
    <div class="save-badge"><span class="save-label">SAVE</span><span class="save-amount">$42</span></div>
  </section>

  <section class="package package-evergreen">
    <h2 class="package-title">Evergreen</h2>
    <p class="package-length">6 week+ package<br>(45 days)</p>
    <p class="package-meals">2 meals per day</p>
    <div class="package-price">$1080.00</div>
    <div class="save-badge"><span class="save-label">SAVE</span><span class="save-amount">$180</span></div>
  </section>
</body>
</html>
```